Catalogue design for Aluminium Panel and spray painting manufacturer based in Huizhou, China.

Metrovan is a trading company that represent Dalong metal spraying industry that manufactures aluminium panels and extrusions of all kinds and PVDF coating.

We are a manufacturer and producer of aluminium panels and PVDF painting based in Huizhou, China. We produce aluminium panels that are use widely in subways, shopping malls and construction works both for interior and exterior usage.

Da Long mainly deal with contractors and project managers business within Mainland China and Hong Kong with a select few clientele in Australia and Philippines. We are now looking to expand the business and reach further international businesses.

We therefore need a new brochure to introduce the new trading name Metrovan to further the sales strategy into international borders. As manufacturers are heavily based on credentials and certifications these must be displayed accordingly to gain trust within the construction market.

The following content will be required

1. Who we are and what we do, manufacturer of aluminium panels and PVDF coating.
2. a)Guide to our manufacturing process, bending, cutting, welding of aluminum panels
b)Guide to choice of painting powder coating or PVDF coating. (PVDF being the main choice)
3. a)Some technical information about the core product of aluminium of aluminum panels such as size dimensions, width of panels and grade of aluminium.
b)Information on PVDF painting and a colour chart of either RAL or PANTONE.
4. Projects undertaken and some photos, preferably in a grid 2 column layout as exampled on attached photo.
5. Certifications of factory and office address and contact info.

We are looking for design that can showcase our manufacturing process in a catalogue displaying a consistent colour design theme throughout.

A simple guide of the manufacturing process and including some technical specification about the aluminium panels such as width and maximum dimenstions etc.

Target Market(s)

Asean and south east asia.

Industry/Entity Type

Manufacturer

Contact Information for Business Card

To be in colour theme with the catalogue design. Contain logo and to draw more focus more on the web url.

Colors
ec1f27

Requirements
Must have
• Must include a colour theme that is striking throughout the catalogue and easy to look at graphical layout. A graphical view without too much text aside from the technical specifications.
• Certifications of manufacturer. ISO, Vetra Kolm etc( as displayed within company profile PDF)
Nice to have
• A consistent usage of photos without too obvious generic building photos.
• A well displayed layout for each page.
• Perhaps a three toned colour theme that works according with the logo. Perhaps some red throughout on a black main colour. Contrasting colours without an overwash of one colour.
Should not have
• Generic photos of office people or overly enthusiastic business people.
• With Exception of photos shots of the factory workers.

```html
<!DOCTYPE html>
<html lang="en">
<head>
<meta charset="utf-8">
<title>Metrovan – Quality Control Process</title>
<link rel="stylesheet" href="https://fonts.googleapis.com/css2?family=Noto+Serif:wght@400;700&family=Open+Sans:wght@300;400;700&display=swap">
<style>
  :root{
    --paper:#e7e8ea;
    --ink:#231f20;
    --red:#dc3446;
    --deep-red:#8e1b22;
    --blue:#3d97d3;
    --lime:#b7d334;
    --orange:#e87734;
    --teal:#178ea3;
    --cyan:#55c6d0;
    --purple:#3b1e4d;
    --tile:#cbb8b0;
  }
  html,body{margin:0;padding:0;width:1200px;height:848px;overflow:hidden;background:var(--paper);}
  .page{display:block;width:1200px;height:848px;}
  .node-label{font-family:"Noto Serif",serif;font-size:9.5px;fill:#fff;text-anchor:middle;}
  .node-label.small{font-size:8px;}
  .node-label.large{font-size:20px;}
  .hex-title{font-family:"Open Sans",sans-serif;font-weight:300;fill:#fff;text-anchor:middle;}
  .flow-tag{font-family:"Open Sans",sans-serif;font-weight:700;font-size:12.5px;fill:var(--ink);}
  .connector{fill:none;stroke:var(--ink);stroke-width:2.5;}
  .connector.thick{stroke-width:4;}
  .step-arrow{fill:var(--ink);}
  .brand-name{font-family:"Noto Serif",serif;font-size:24px;fill:var(--deep-red);}
  .page-number{font-family:"Open Sans",sans-serif;font-weight:700;font-size:40px;fill:#fff;text-anchor:middle;}
</style>
</head>
<body>
<svg class="page" viewBox="0 0 1300 919" xmlns="http://www.w3.org/2000/svg">
  <defs>
    <radialGradient id="tile-glow" cx="50%" cy="50%" r="50%">
      <stop offset="0" stop-color="#ffffff" stop-opacity="0.5"/>
      <stop offset="0.35" stop-color="var(--tile)" stop-opacity="0.55"/>
      <stop offset="1" stop-color="var(--tile)" stop-opacity="0"/>
    </radialGradient>
    <path id="down" d="M-7,0 L7,0 L0,12Z"/>
    <marker id="head" viewBox="0 0 10 10" refX="8" refY="5" markerWidth="10" markerHeight="10" markerUnits="userSpaceOnUse" orient="auto">
      <path d="M0,0 L10,5 L0,10Z" fill="var(--ink)"/>
    </marker>
  </defs>

  <!-- page background -->
  <rect width="1300" height="919" fill="var(--paper)"/>
  <g role="img" aria-label="Decorative radial tile pattern in warm grey">
    <ellipse cx="800" cy="470" rx="560" ry="460" fill="url(#tile-glow)"/>
  </g>

  <!-- corner band -->
  <polygon points="0,0 210,0 18,160 0,160" fill="#262626"/>
  <polygon points="210,0 226,0 18,165 18,150" fill="var(--deep-red)"/>

  <!-- intake -->
  <polygon points="608,87 635,40 691,40 718,87 691,135 635,135" fill="var(--red)"/>
  <text class="node-label small" x="663" y="89">CUSTOMER SUPPLY<tspan x="663" dy="10">MATERIAL</tspan></text>
  <rect x="583" y="133" width="160" height="22" rx="11" fill="var(--red)"/>
  <text class="node-label" x="663" y="147.5">Warehouse Acceptance (Quantity)</text>
  <use href="#down" x="662" y="161" class="step-arrow"/>
  <rect x="590" y="177" width="147" height="22" rx="11" fill="var(--blue)"/>
  <text class="node-label" x="663" y="191.5">Wait For Inspection Area</text>
  <use href="#down" x="662" y="205" class="step-arrow"/>

  <!-- incoming quality control -->
  <polygon points="610,268 638,220 690,220 718,268 690,316 638,316" fill="var(--lime)"/>
  <text class="hex-title" x="664" y="279" font-size="30">IQC</text>
  <text class="flow-tag" x="582" y="259">OK</text>
  <path class="connector" d="M610,266 H362 V314" marker-end="url(#head)"/>
  <text class="flow-tag" x="715" y="256">NO</text>
  <path d="M724,260 L740,268 L724,276Z" class="step-arrow"/>
  <rect x="743" y="245" width="90" height="44" rx="12" fill="var(--orange)"/>
  <text class="node-label" x="788" y="270">Fail Label</text>
  <path class="connector thick" d="M838,268 H862" marker-end="url(#head)"/>
  <path d="M850,259 L866,268 L850,277Z" class="step-arrow"/>

  <rect x="877" y="257" width="131" height="30" rx="12" fill="var(--teal)"/>
  <text class="node-label" x="942" y="275">Wait For Improving Area</text>
  <use href="#down" x="942" y="294" class="step-arrow"/>
  <rect x="877" y="313" width="131" height="32" rx="12" fill="var(--teal)"/>
  <text class="node-label" x="942" y="326">Incoming Material<tspan x="942" dy="10">Inspection Report</tspan></text>
  <use href="#down" x="942" y="351" class="step-arrow"/>
  <rect x="877" y="369" width="131" height="44" rx="14" fill="var(--teal)"/>
  <text class="node-label" x="942" y="389">Communicate With<tspan x="942" dy="10">Customers</tspan></text>
  <path class="connector" d="M877,391 H780 V333 H446" marker-end="url(#head)"/>
  <path class="connector thick" d="M942,413 V462"/>
  <use href="#down" x="942" y="460" class="step-arrow"/>
  <rect x="961" y="424" width="46" height="47" fill="var(--teal)"/>
  <text class="node-label" x="984" y="454" font-size="18" font-family="Open Sans, sans-serif">NO</text>
  <rect x="884" y="483" width="118" height="65" fill="var(--orange)"/>
  <text class="node-label large" x="943" y="512">Returned<tspan x="943" dy="18">Goods</tspan></text>

  <!-- painting line -->
  <rect x="291" y="320" width="147" height="23" rx="11" fill="var(--lime)"/>
  <text class="node-label" x="365" y="335">Pass Label</text>
  <use href="#down" x="365" y="349" class="step-arrow"/>
  <rect x="291" y="368" width="147" height="22" rx="11" fill="var(--blue)"/>
  <text class="node-label" x="365" y="382.5">Qualified Area</text>
  <use href="#down" x="365" y="397" class="step-arrow"/>
  <path class="connector" d="M405,390 V403 H731 V428" marker-end="url(#head)"/>

  <rect x="300" y="413" width="131" height="47" rx="14" fill="var(--blue)"/>
  <text class="node-label" x="365" y="440">Painting &amp; Silk Printing</text>
  <text class="flow-tag" x="449" y="427">Self Inspection</text>
  <path class="connector" d="M603,776 V437 H436" marker-end="url(#head)"/>
  <path class="connector" d="M400,473 H603"/>
  <path class="connector" d="M592,790 V488 H400 V466" marker-end="url(#head)"/>
  <use href="#down" x="365" y="466" class="step-arrow"/>

  <polygon points="336,512 350,485 380,485 394,512 380,539 350,539" fill="var(--red)"/>
  <text class="hex-title" x="365" y="520" font-size="20">QA</text>
  <text class="flow-tag" x="319" y="544">OK</text>
  <text class="flow-tag" x="461" y="556">NO</text>
  <path class="connector" d="M394,512 H515 V561" marker-end="url(#head)"/>
  <use href="#down" x="365" y="546" class="step-arrow"/>

  <rect x="318" y="569" width="95" height="28" fill="var(--red)"/>
  <text class="node-label" x="365" y="586">Pass Label</text>
  <use href="#down" x="365" y="604" class="step-arrow"/>
  <rect x="318" y="623" width="95" height="28" fill="var(--red)"/>
  <text class="node-label" x="365" y="640">Qualified Area</text>
  <use href="#down" x="365" y="660" class="step-arrow"/>
  <rect x="325" y="678" width="81" height="37" fill="var(--red)"/>
  <text class="node-label" x="365" y="699">Package</text>
  <use href="#down" x="365" y="721" class="step-arrow"/>
  <rect x="325" y="739" width="81" height="36" fill="var(--red)"/>
  <text class="node-label" x="365" y="760">Storage</text>
  <use href="#down" x="365" y="778" class="step-arrow"/>
  <circle cx="365" cy="817" r="33" fill="var(--red)"/>
  <text class="node-label" x="365" y="821">Delivery</text>

  <rect x="468" y="569" width="94" height="28" fill="var(--cyan)"/>
  <text class="node-label" x="515" y="586">Fail Label</text>
  <use href="#down" x="515" y="604" class="step-arrow"/>
  <rect x="468" y="624" width="94" height="28" fill="var(--cyan)"/>
  <text class="node-label" x="515" y="641">Unqualified</text>
  <use href="#down" x="515" y="659" class="step-arrow"/>
  <rect x="468" y="679" width="94" height="44" fill="var(--cyan)"/>
  <text class="node-label" x="515" y="699">QC Inspection<tspan x="515" dy="10">Report</tspan></text>
  <rect x="562" y="696" width="56" height="9" fill="var(--cyan)"/>
  <text class="flow-tag" x="440" y="741">Tiny Defect</text>
  <use href="#down" x="515" y="729" class="step-arrow"/>
  <rect x="468" y="748" width="94" height="65" fill="var(--cyan)"/>
  <text class="node-label" x="515" y="777">Concessions<tspan x="515" dy="10">Report</tspan></text>
  <text class="flow-tag" x="441" y="762">OK</text>
  <path class="connector" d="M468,776 H431 V581 H411" marker-end="url(#head)"/>
  <text class="flow-tag" x="567" y="804">NO</text>
  <path class="connector" d="M562,790 H592"/>

  <!-- sheet metal line -->
  <rect x="691" y="436" width="81" height="36" fill="var(--orange)"/>
  <text class="node-label" x="731" y="451">Sheet Metal<tspan x="731" dy="10">Fabrication</tspan></text>
  <use href="#down" x="731" y="478" class="step-arrow"/>
  <polygon points="704,521 717,496 748,496 761,521 748,547 717,547" fill="var(--purple)"/>
  <text class="hex-title" x="732" y="528" font-size="18">QC</text>
  <text class="flow-tag" x="631" y="561">OK</text>
  <text class="flow-tag" x="753" y="549">NO</text>
  <path class="connector" d="M704,521 H665 V568" marker-end="url(#head)"/>
  <path class="connector" d="M761,521 H799 V568" marker-end="url(#head)"/>

  <rect x="617" y="576" width="95" height="28" fill="var(--purple)"/>
  <text class="node-label" x="664" y="593">Pass Label</text>
  <use href="#down" x="664" y="611" class="step-arrow"/>
  <rect x="617" y="630" width="95" height="28" fill="var(--purple)"/>
  <text class="node-label" x="664" y="642">Qualified Area<tspan x="664" dy="10">Product</tspan></text>
  <use href="#down" x="664" y="665" class="step-arrow"/>
  <rect x="617" y="685" width="94" height="65" fill="var(--purple)"/>
  <text class="node-label" x="664" y="715" font-size="11">Semi-Finished In<tspan x="664" dy="12">Storage</tspan></text>
  <text class="flow-tag" x="605" y="765">OK</text>

  <rect x="752" y="576" width="95" height="28" fill="var(--red)"/>
  <text class="node-label" x="799" y="593">Fail Label</text>
  <use href="#down" x="799" y="611" class="step-arrow"/>
  <rect x="752" y="630" width="95" height="28" fill="var(--red)"/>
  <text class="node-label" x="799" y="647">Unqualified Area</text>
  <use href="#down" x="799" y="665" class="step-arrow"/>
  <rect x="752" y="683" width="95" height="44" fill="var(--red)"/>
  <text class="node-label" x="799" y="702">QC Inspection<tspan x="799" dy="10">Report</tspan></text>
  <rect x="847" y="701" width="20" height="9" fill="var(--red)"/>
  <text class="flow-tag" x="726" y="749">Tiny Defect</text>
  <use href="#down" x="799" y="733" class="step-arrow"/>
  <rect x="752" y="754" width="95" height="44" fill="var(--red)"/>
  <text class="node-label" x="799" y="773">Concessions<tspan x="799" dy="10">Report</tspan></text>
  <path class="connector" d="M752,776 H603"/>
  <text class="flow-tag" x="870" y="742">NO</text>
  <text class="flow-tag" x="780" y="436">OK</text>
  <path class="connector" d="M847,777 H868 V451 H780" marker-end="url(#head)"/>

  <!-- footer -->
  <rect x="87" y="850" width="42" height="40" rx="4" fill="var(--red)"/>
  <text class="brand-name" x="138" y="878">Metrovan</text>
  <rect x="250" y="867" width="865" height="6" fill="#262626"/>
  <rect x="1138" y="847" width="77" height="72" fill="#262626"/>
  <polygon points="1138,847 1158,847 1138,867" fill="var(--deep-red)"/>
  <text class="page-number" x="1178" y="898">4</text>
</svg>
</body>
</html>
```